Business Card and Letterhead Design for Public Accounting Firm

Business card and letterhead design for a CPA Firm located in Orange County, CA. We're looking for a modern and professional design utilizing our existing logo. We'd like a clean "less is more" look, but also something that catches the eye. We provide a high level of service to our clients. Open to single or double sided business cards.

Additional info: color numbers on logo
Blue :
R 0
G 83
B 125

#00537D

Silver :

R 154
G 154
B 154

#9A9A9A

Target Market(s)

Businesses and individuals

Industry/Entity Type

Accounting

Contact Information for Business Card

Moss Whitfield & Danby LLP - 4827 Larkspur Vale Road, Irvine, CA 92614 - (949)731-2864 - mwdaccts.example

Font styles to use
Serif
Sans Serif
Other font styles liked:
• See font file uploaded

Colors
0054AA
0677BA
7BADD7
CADEEF
E8F1F8

Requirements
Nice to have
• Possibly use the font file provided which matches our logo, but adjust to be not in all caps

```html
<!DOCTYPE html>
<html lang="en">
<head>
<meta charset="utf-8">
<title>Moss Whitfield &amp; Danby LLP — Letterhead</title>
<link rel="stylesheet" href="https://fonts.googleapis.com/css2?family=Open+Sans:wght@300;400;600&display=swap">
<style>
  :root {
    --brand-blue: #1d5f86;
    --brand-silver: #9a9a9a;
    --ink: #3a3a3a;
    --paper: #ffffff;
    --paper-shade: #f1f1f1;
    --backdrop: #d9d9d9;
    --signature-tone: #e4e4e4;
  }
  * { box-sizing: border-box; margin: 0; padding: 0; }
  html, body {
    width: 1146px; height: 1200px; overflow: hidden;
    background: var(--backdrop);
  }
  .letterhead {
    position: absolute; left: 141px; top: 40px;
    width: 864px; height: 1120px;
    background: linear-gradient(160deg, var(--paper) 30%, var(--paper-shade) 100%);
    box-shadow: 4px 6px 14px rgba(0,0,0,0.28);
    font-family: "Open Sans", sans-serif;
    color: var(--ink);
  }
  .letterhead__brand {
    position: absolute; left: 70px; top: 80px;
    display: flex; align-items: center; gap: 12px;
  }
  .brand-mark {
    width: 18px; height: 18px; background: var(--brand-blue);
  }
  .brand-name {
    font-size: 26px; font-weight: 600; color: var(--brand-blue);
    letter-spacing: 0.5px;
  }
  .letter {
    position: absolute; left: 70px; top: 262px; width: 727px;
    font-size: 14.2px; font-weight: 300; line-height: 21px;
  }
  .letter p { margin-bottom: 21px; text-align: justify; }
  .letter .salutation, .letter .closing { text-align: left; }
  .signature {
    width: 102px; height: 96px; margin: 2px 0 26px;
    background: var(--signature-tone);
  }
  .signatory { line-height: 21px; }
  .letter-footer {
    position: absolute; left: 0; top: 1045px; width: 864px; height: 32px;
    display: flex;
  }
  .letter-footer__contact {
    width: 701px; background: var(--brand-blue); color: #fff;
    display: flex; align-items: center; padding-left: 64px; gap: 18px;
    font-size: 13px; font-weight: 400;
  }
  .contact-item { display: flex; align-items: center; gap: 5px; }
  .contact-item svg { width: 15px; height: 15px; }
  .letter-footer__brand {
    margin-left: auto; padding-right: 14px;
    font-size: 13px; font-weight: 600;
  }
  .letter-footer__web {
    flex: 1; background: var(--brand-silver); color: #fff;
    display: flex; align-items: center; padding-left: 10px;
    font-size: 12px; font-weight: 600;
  }
</style>
</head>
<body>
  <main class="letterhead">
    <header class="letterhead__brand">
      <span class="brand-mark"></span>
      <span class="brand-name">Moss Whitfield &amp; Danby LLP</span>
    </header>

    <section class="letter">
      <p class="salutation">Dear customer,</p>
      <p>Lorem ipsum dolor sit amet, consectetur adipisicing elit, sed do eiusmod tempor incididunt ut labore et dolore magna aliqua. Ut enim ad minim veniam, quis nostrud exercitation ullamco laboris nisi ut aliquip ex ea commodo consequat. Duis aute irure dolor in reprehenderit in voluptate velit esse cillum dolore eu fugiat nulla pariatur. Excepteur sint occaecat cupidatat non proident, sunt in culpa qui officia deserunt mollit anim id est laborum.</p>
      <p>Lorem ipsum dolor sit amet, consectetur adipisicing elit, sed do eiusmod tempor incididunt ut labore et dolore magna aliqua. Ut enim ad minim veniam, quis nostrud exercitation ullamco laboris nisi ut aliquip ex ea commodo consequat. Duis aute irure dolor in reprehenderit in voluptate velit esse cillum dolore eu fugiat nulla pariatur. Excepteur sint occaecat cupidatat non proident, sunt in culpa qui officia deserunt mollit anim id est laborum.</p>
      <p>Lorem ipsum dolor sit amet, consectetur adipisicing elit, sed do eiusmod tempor incididunt ut labore et dolore magna aliqua. Ut enim ad minim veniam, quis nostrud exercitation ullamco laboris nisi ut aliquip ex ea commodo consequat. Duis aute irure dolor in reprehenderit in voluptate velit esse cillum dolore eu fugiat nulla pariatur. Excepteur sint occaecat cupidatat non proident, sunt in culpa qui officia deserunt mollit anim id est laborum.</p>
      <p class="closing">Yours Sincerely,</p>
      <div class="signature" role="img" aria-label="Handwritten signature of Aaron Pell"></div>
      <div class="signatory">Aaron Pell<br>General Director</div>
    </section>

    <footer class="letter-footer">
      <div class="letter-footer__contact">
        <span class="contact-item">
          <svg viewBox="0 0 16 16" fill="none" stroke="#fff" stroke-width="1.2">
            <circle cx="8" cy="8" r="7"/>
            <path d="M5.2 4.3l1.3-.3.8 1.8-.9.7c.5 1.1 1.3 1.9 2.3 2.4l.7-.9 1.8.8-.3 1.3c-3 .2-5.8-2.8-5.7-5.8z" fill="#fff" stroke="none"/>
          </svg>
          (949) 731-2864
        </span>
        <span class="contact-item">
          <svg viewBox="0 0 16 16" fill="none" stroke="#fff" stroke-width="1.2">
            <circle cx="8" cy="8" r="7"/>
            <path d="M8 12.2s-2.6-2.8-2.6-4.7a2.6 2.6 0 0 1 5.2 0c0 1.9-2.6 4.7-2.6 4.7z"/>
            <circle cx="8" cy="7.4" r="0.9" fill="#fff" stroke="none"/>
          </svg>
          4827 Larkspur Vale Road, Irvine, CA 92614
        </span>
        <span class="letter-footer__brand">Moss Whitfield &amp; Danby LLP</span>
      </div>
      <div class="letter-footer__web">mwdaccts.example</div>
    </footer>
  </main>
</body>
</html>
```